Yumm... Caramel packaging

We want to create a derivative of our gummies packaging for our new product, our chewable caramel. We would like to use a caramel, brownish, cream pallet. With hints of green. See example1.pdf for an example of the colors, they DO NOT have to be exact. Check YUMM Dulce de Leche.psd for the logo with approximated colors, you can change these, but please keep logo structure. 3.62x4.50x1.50.pdf is the guideline for the packaging print, this includes size and print area. All Gummies Mock up.jpg is our gummies packaging line up, mocked up. All warnings must be included, use this as guide.

Designers are asking for more time, and i want higher quiality submissions.

```html
<!DOCTYPE html>
<html lang="en">
<head>
<meta charset="utf-8">
<title>Yumm Chewable Caramel – Pouch Artwork</title>
<link rel="stylesheet" href="https://fonts.googleapis.com/css2?family=Open+Sans:wdth,wght@75..100,400..800&family=Arimo:wght@400;700&display=swap">
<style>
  :root {
    --paper: #ffffff;
    --white-side: #f4f4f4;
    --caramel: #a9692f;
    --caramel-art: #ad763a;
    --caramel-light: #d59b52;
    --tan: #c9a98a;
    --gusset-white: #f1f1f1;
    --green: #1f5a2e;
    --green-faded: #6f8f76;
    --ink: #5d5e60;
    --dim: #555659;
    --safe: #e0262b;
    --bleed: #8cc63f;
    --guide: #6b6b6b;
    --tag: #5f6062;
  }
  html, body { margin: 0; padding: 0; }
  body {
    width: 1200px; height: 2697px; overflow: hidden;
    background: var(--paper);
    font-family: "Open Sans", sans-serif;
  }
  .sheet { display: block; width: 1200px; height: 2697px; }
  .cond { font-family: "Open Sans", sans-serif; font-stretch: 75%; }
  .brand { font-family: "Open Sans", sans-serif; font-weight: 800; fill: var(--ink); }
  .title { font-family: "Arimo", sans-serif; font-weight: 700; fill: var(--dim); }
  .dim-label { font-family: "Arimo", sans-serif; font-weight: 700; fill: var(--dim); }
  .fill-white { fill: var(--white-side); }
  .fill-caramel { fill: var(--caramel); }
  .fill-caramel-art { fill: var(--caramel-art); }
  .fill-tan { fill: var(--tan); }
  .fill-gusset { fill: var(--gusset-white); }
  .fill-paper { fill: var(--paper); }
  .label-circle { fill: var(--caramel-light); stroke: #c98a44; stroke-width: 4; }
  .label-text { fill: var(--paper); font-weight: 700; }
  .sticker-box { fill: none; stroke: var(--green); stroke-width: 2; stroke-dasharray: 8 5; }
  .sticker-head { fill: var(--green); font-weight: 700; }
  .sticker-note { fill: #8a8a8a; font-weight: 600; }
  .warn-green { fill: var(--green); font-weight: 700; }
  .warn-white { fill: var(--paper); font-weight: 700; }
  .warn-faded { fill: var(--green-faded); font-weight: 700; }
  .badge { fill: var(--paper); }
  .badge-cross { fill: var(--caramel); }
  .dim-line { stroke: var(--dim); stroke-width: 1.5; fill: none; }
  .guide-dash { stroke: var(--guide); stroke-width: 1.5; stroke-dasharray: 9 6; fill: none; }
  .zipper-line { stroke: var(--guide); stroke-width: 3; }
  .bleed-frame { fill: none; stroke: var(--bleed); stroke-width: 3; }
  .safe-frame { fill: none; stroke: var(--safe); stroke-width: 3; }
  .gusset-mark { fill: none; stroke: #d8d8d8; stroke-width: 3; }
  .tag-shape { fill: var(--tag); }
  .tag-text { fill: #fff; font-family: "Arimo", sans-serif; font-weight: 700; }
</style>
</head>
<body>
<svg class="sheet" viewBox="0 0 1200 2697" xmlns="http://www.w3.org/2000/svg">
  <defs>
    <linearGradient id="caramel-swirl" x1="0" y1="0" x2="1" y2="1">
      <stop offset="0" stop-color="#c98a44"/>
      <stop offset="0.5" stop-color="#e0b16e"/>
      <stop offset="1" stop-color="#b27434"/>
    </linearGradient>
    <clipPath id="front-left"><rect x="0" y="0" width="693" height="1200"/></clipPath>
    <clipPath id="front-right"><rect x="693" y="0" width="600" height="1200"/></clipPath>
    <clipPath id="art-left"><rect x="0" y="1300" width="676" height="1400"/></clipPath>
    <clipPath id="art-right"><rect x="676" y="1300" width="600" height="1400"/></clipPath>
    <clipPath id="strip-left"><rect x="248" y="1405" width="64" height="1205"/></clipPath>
    <clipPath id="strip-right"><rect x="910" y="1405" width="64" height="1205"/></clipPath>
  </defs>

  <!-- ===== Front panel (flat) ===== -->
  <g class="pouch-front">
    <path class="fill-white" d="M176 122 H693 V1100 H240 Q228 1100 226 1088 L188 300 L176 122 Z"/>
    <path class="fill-caramel" d="M693 122 H1035 L1022 300 L972 1088 Q970 1100 958 1100 H693 Z"/>

    <text class="brand" font-size="86" transform="translate(560 650) rotate(-90)">Yumm</text>
    <circle cx="531" cy="685" r="14" fill="var(--green)"/>

    <rect x="615" y="370" width="156" height="412" rx="78" fill="url(#caramel-swirl)" stroke="#c98a44" stroke-width="4"
          role="img" aria-label="Caramel swirl illustration"/>
    <circle class="label-circle" cx="693" cy="455" r="62"/>
    <text class="cond label-text" font-size="27" text-anchor="middle" x="693" y="448">CHEWABLE</text>
    <text class="cond label-text" font-size="27" text-anchor="middle" x="693" y="477">CARAMEL</text>

    <rect class="sticker-box" x="272" y="792" width="303" height="116"/>
    <text class="cond sticker-head" font-size="21" x="286" y="832">POTENCY :</text>
    <text class="cond sticker-head" font-size="21" x="286" y="858">FLAVORS :</text>
    <text class="cond sticker-head" font-size="21" x="286" y="884">PIECES :</text>
    <text class="cond sticker-note" font-size="22" x="480" y="842" text-anchor="middle">STICKER</text>
    <text class="cond sticker-note" font-size="22" x="480" y="870" text-anchor="middle">AREA</text>

    <circle class="badge" cx="842" cy="843" r="56"/>
    <rect class="badge-cross" x="830" y="810" width="24" height="66"/>
    <rect class="badge-cross" x="809" y="831" width="66" height="24"/>

    <g clip-path="url(#front-left)">
      <text class="cond warn-green" font-size="31" text-anchor="middle" x="610" y="992">Contains Medical Cannabis. This product complies with all</text>
      <text class="cond warn-green" font-size="31" text-anchor="middle" x="610" y="1027">mandatory contaminant testing. Keep out of reach of children.</text>
    </g>
    <g clip-path="url(#front-right)">
      <text class="cond warn-white" font-size="31" text-anchor="middle" x="610" y="992">Contains Medical Cannabis. This product complies with all</text>
      <text class="cond warn-white" font-size="31" text-anchor="middle" x="610" y="1027">mandatory contaminant testing. Keep out of reach of children.</text>
    </g>
  </g>

  <!-- ===== Artwork dieline ===== -->
  <text class="title" font-size="72" text-anchor="middle" x="611" y="1232">ARTWORK</text>

  <g class="dimensions-top">
    <line class="dim-line" x1="248" y1="1287" x2="974" y2="1287"/>
    <path d="M248 1287 l12 -5 v10 Z M974 1287 l-12 -5 v10 Z" fill="var(--dim)"/>
    <rect x="515" y="1272" width="192" height="30" fill="#fff"/>
    <text class="dim-label" font-size="20" text-anchor="middle" x="611" y="1294">3.62" [ 91.95mm ]</text>
    <line x1="248" y1="1272" x2="248" y2="1382" class="dim-line"/>
    <line x1="974" y1="1272" x2="974" y2="1382" class="dim-line"/>

    <line class="dim-line" x1="248" y1="1335" x2="974" y2="1335"/>
    <line class="dim-line" x1="312" y1="1322" x2="312" y2="1382"/>
    <line class="dim-line" x1="910" y1="1322" x2="910" y2="1382"/>
    <rect x="258" y="1322" width="45" height="26" fill="#fff"/>
    <text class="dim-label" font-size="14" x="280" y="1340" text-anchor="middle">8mm</text>
    <rect x="918" y="1322" width="46" height="26" fill="#fff"/>
    <text class="dim-label" font-size="14" x="942" y="1340" text-anchor="middle">8mm</text>
    <rect x="515" y="1320" width="192" height="30" fill="#fff"/>
    <text class="dim-label" font-size="20" text-anchor="middle" x="611" y="1342">2.99" [ 75.95mm ]</text>
  </g>

  <g class="dieline">
    <rect class="fill-gusset" x="248" y="1405" width="428" height="1205"/>
    <rect class="fill-tan" x="676" y="1405" width="298" height="1205"/>
    <rect x="248" y="1405" width="64" height="1205" fill="#efefef"/>
    <path class="fill-paper" d="M312 1405 H676 V2200 Q480 2210 312 2155 Z"/>
    <path class="fill-caramel-art" d="M676 1405 H910 V2155 Q800 2200 676 2200 Z"/>
    <line x1="248" y1="2307" x2="974" y2="2307" stroke="#dcdcdc" stroke-width="1.5"/>
    <line x1="312" y1="1405" x2="312" y2="2610" stroke="#e3e3e3" stroke-width="1"/>
    <line x1="910" y1="1405" x2="910" y2="2610" stroke="#bda084" stroke-width="1"/>
    <path class="fill-paper" d="M312 2485 Q480 2370 676 2370 V2600 Q480 2600 312 2485 Z"/>
    <path class="fill-caramel-art" d="M676 2370 Q800 2375 910 2485 Q800 2580 676 2600 Z"/>

    <g clip-path="url(#strip-left)">
      <circle class="gusset-mark" cx="255" cy="2212" r="46"/>
      <circle class="gusset-mark" cx="255" cy="2412" r="46"/>
      <circle class="gusset-mark" cx="255" cy="2512" r="46"/>
    </g>
    <g clip-path="url(#strip-right)">
      <circle class="gusset-mark" cx="968" cy="2212" r="46"/>
      <circle class="gusset-mark" cx="968" cy="2412" r="46"/>
      <circle class="gusset-mark" cx="968" cy="2512" r="46"/>
    </g>

    <line class="guide-dash" x1="260" y1="1515" x2="962" y2="1515"/>
    <path d="M248 1507 h12 l12 8 l-12 8 h-12 Z M974 1507 h-12 l-12 8 l12 8 h12 Z" fill="var(--guide)"/>
    <line class="guide-dash" x1="312" y1="1565" x2="910" y2="1565"/>
    <line class="zipper-line" x1="312" y1="1652" x2="910" y2="1652"/>
    <line class="zipper-line" x1="312" y1="1677" x2="910" y2="1677"/>
    <line class="guide-dash" x1="312" y1="1765" x2="910" y2="1765"/>

    <text class="brand" font-size="64" transform="translate(573 1940) rotate(-90)">Yumm</text>
    <circle cx="566" cy="1945" r="10" fill="var(--green)"/>

    <rect x="617" y="1725" width="120" height="325" rx="60" fill="url(#caramel-swirl)" stroke="#c98a44" stroke-width="3"
          role="img" aria-label="Caramel swirl illustration"/>
    <circle class="label-circle" cx="677" cy="1792" r="48"/>
    <text class="cond label-text" font-size="21" text-anchor="middle" x="677" y="1787">CHEWABLE</text>
    <text class="cond label-text" font-size="21" text-anchor="middle" x="677" y="1809">CARAMEL</text>

    <circle class="badge" cx="793" cy="2097" r="43"/>
    <rect class="badge-cross" x="784" y="2071" width="18" height="52"/>
    <rect class="badge-cross" x="767" y="2088" width="52" height="18"/>

    <rect class="sticker-box" x="348" y="2058" width="238" height="92" stroke-width="1.5"/>
    <text class="cond sticker-head" font-size="16" x="360" y="2090">POTENCY :</text>
    <text class="cond sticker-head" font-size="16" x="360" y="2111">FLAVORS :</text>
    <text class="cond sticker-head" font-size="16" x="360" y="2132">PIECES :</text>
    <text class="cond sticker-note" font-size="17" x="512" y="2098" text-anchor="middle">STICKER</text>
    <text class="cond sticker-note" font-size="17" x="512" y="2120" text-anchor="middle">AREA</text>

    <g clip-path="url(#art-left)">
      <text class="cond warn-faded" font-size="24" text-anchor="middle" x="611" y="2213">Contains Medical Cannabis. This product complies with all</text>
      <text class="cond warn-faded" font-size="24" text-anchor="middle" x="611" y="2241">mandatory contaminant testing. Keep out of reach of children.</text>
    </g>
    <g clip-path="url(#art-right)">
      <text class="cond warn-white" font-size="24" text-anchor="middle" x="611" y="2213">Contains Medical Cannabis. This product complies with all</text>
      <text class="cond warn-white" font-size="24" text-anchor="middle" x="611" y="2241">mandatory contaminant testing. Keep out of reach of children.</text>
    </g>

    <path class="safe-frame" d="M336 1430 H885 V2143 Q611 2285 336 2143 Z"/>
    <path class="bleed-frame" d="M224 2610 V1382 H999 V2610"/>
  </g>

  <g class="dimensions-left">
    <line class="dim-line" x1="40" y1="1405" x2="248" y2="1405"/>
    <line class="dim-line" x1="115" y1="2307" x2="224" y2="2307"/>
    <line class="dim-line" x1="160" y1="1565" x2="224" y2="1565"/>
    <line class="dim-line" x1="160" y1="1765" x2="224" y2="1765"/>

    <line class="dim-line" x1="57" y1="1405" x2="57" y2="2610"/>
    <path d="M57 1405 l-5 12 h10 Z" fill="var(--dim)"/>
    <rect x="42" y="2355" width="30" height="215" fill="#fff"/>
    <text class="dim-label" font-size="21" text-anchor="middle" transform="translate(64 2462) rotate(-90)">10.50" [ 266.70mm ]</text>

    <line class="dim-line" x1="126" y1="1405" x2="126" y2="2610"/>
    <path d="M126 1405 l-5 12 h10 Z M126 2307 l-5 -12 h10 Z M126 2307 l-5 12 h10 Z M126 2610 l-5 -12 h10 Z" fill="var(--dim)"/>
    <rect x="111" y="1760" width="30" height="200" fill="#fff"/>
    <text class="dim-label" font-size="21" text-anchor="middle" transform="translate(133 1860) rotate(-90)">4.50" [ 114.30mm ]</text>
    <rect x="111" y="2370" width="30" height="180" fill="#fff"/>
    <text class="dim-label" font-size="21" text-anchor="middle" transform="translate(133 2460) rotate(-90)">1.50" [ 38.10mm ]</text>

    <line class="dim-line" x1="176" y1="1405" x2="176" y2="1765"/>
    <path d="M176 1405 l-4 9 h8 Z M176 1565 l-4 -9 h8 Z M176 1565 l-4 9 h8 Z M176 1765 l-4 -9 h8 Z" fill="var(--dim)"/>
    <rect x="166" y="1425" width="20" height="120" fill="#fff"/>
    <text class="dim-label" font-size="13" text-anchor="middle" transform="translate(181 1485) rotate(-90)">0.79" [ 20.07mm ]</text>
    <rect x="166" y="1600" width="20" height="130" fill="#fff"/>
    <text class="dim-label" font-size="13" text-anchor="middle" transform="translate(181 1665) rotate(-90)">1.00" [ 25.40mm ]</text>
  </g>

  <g class="callouts">
    <path class="tag-shape" d="M1035 1517 L1054 1495 H1158 Q1162 1495 1162 1499 V1536 Q1162 1540 1158 1540 H1054 Z"/>
    <text class="tag-text" font-size="20" text-anchor="middle" x="1106" y="1514">tear</text>
    <text class="tag-text" font-size="20" text-anchor="middle" x="1106" y="1535">notch</text>
    <path class="tag-shape" d="M1035 1665 L1054 1643 H1158 Q1162 1643 1162 1647 V1684 Q1162 1688 1158 1688 H1054 Z"/>
    <text class="tag-text" font-size="21" text-anchor="middle" x="1106" y="1673">zipper</text>
  </g>
</svg>
</body>
</html>
```